" Trabalhamos com vistorias profissionais de imóveis. Um vistoriador (engenheiro civil ou alguém com experiência em obras e entregas de imóveis) analisa detalhadamente o imóvel, buscando e relatando vícios construtivos. Todo trabalho é documentado através de relatório, que servirá de garantia futura para as partes interessadas. Nossa ideia principal é a de que vistoriar corretamente um imóvel pode significar enorme economia e evitar muita dor de cabeça futura. "

```html
<!DOCTYPE html>
<html lang="pt-BR">
<head>
<meta charset="utf-8">
<title>Assinatura de e-mail – Prumo Engenharia</title>
<link rel="stylesheet" href="https://fonts.googleapis.com/css2?family=Montserrat:wght@500;600;700&display=swap">
<style>
  :root {
    --navy: #1b2a4e;
    --orange: #e8622c;
    --white: #ffffff;
    --page: #eef0f3;
    --muted: #6b7488;
  }
  * { box-sizing: border-box; margin: 0; padding: 0; }
  html, body {
    width: 1200px; height: 1200px; overflow: hidden;
    background: var(--page);
    font-family: "Montserrat", Arial, sans-serif;
  }
  .signature {
    position: absolute; left: 100px; top: 400px;
    width: 1000px; height: 400px;
    background: var(--white);
    overflow: hidden;
    box-shadow: 0 4px 18px rgba(0,0,0,0.08);
  }
  .signature__band { position: absolute; inset: 0; }
  .brand {
    position: absolute; left: 50px; top: 70px;
    display: flex; align-items: center; gap: 16px;
  }
  .brand__mark {
    width: 22px; height: 22px;
    background: var(--orange);
  }
  .brand__name {
    color: var(--navy); font-weight: 700;
    font-size: 34px; letter-spacing: 0.5px;
  }
  .person {
    position: absolute; right: 60px; top: 62px; text-align: right;
    color: var(--navy);
  }
  .person__name { font-weight: 700; font-size: 26px; letter-spacing: 0.5px; }
  .person__role { font-weight: 600; font-size: 14px; letter-spacing: 2px; color: var(--muted); margin-top: 4px; }
  .contacts {
    position: absolute; right: 34px; top: 196px;
    list-style: none; color: var(--white);
    font-weight: 500; font-size: 15px; text-align: right;
  }
  .contacts li { display: flex; align-items: center; justify-content: flex-end; gap: 12px; height: 28px; }
  .contacts svg { width: 16px; height: 16px; fill: var(--orange); flex: none; }
  .contacts .contacts__address { height: auto; align-items: flex-start; line-height: 22px; margin-top: 8px; }
  .website {
    position: absolute; left: 60px; bottom: 40px;
    color: var(--white); font-weight: 600; font-size: 19px; letter-spacing: 2px;
  }
</style>
</head>
<body>
  <div class="signature">
    <svg class="signature__band" viewBox="0 0 1000 400" preserveAspectRatio="none" aria-hidden="true">
      <path d="M0,275 L390,275 C465,275 475,160 555,160 L1000,160 L1000,400 L0,400 Z" fill="var(--navy)"/>
    </svg>

    <div class="brand">
      <span class="brand__mark"></span>
      <span class="brand__name">Prumo Engenharia</span>
    </div>

    <div class="person">
      <div class="person__name">NOME SOBRENOME</div>
      <div class="person__role">FUNÇÃO</div>
    </div>

    <ul class="contacts">
      <li>00 00000.0000 | 00000.0000
        <svg viewBox="0 0 24 24"><path d="M6.6 10.8a15.1 15.1 0 0 0 6.6 6.6l2.2-2.2a1 1 0 0 1 1-.25 11.4 11.4 0 0 0 3.6.57 1 1 0 0 1 1 1V20a1 1 0 0 1-1 1A17 17 0 0 1 3 4a1 1 0 0 1 1-1h3.5a1 1 0 0 1 1 1c0 1.25.2 2.45.57 3.57a1 1 0 0 1-.25 1z"/></svg>
      </li>
      <li>contato@prumoengenharia.com.br
        <svg viewBox="0 0 24 24"><path d="M3 5h18v14H3z M3 5l9 7 9-7" fill="none" stroke="var(--orange)" stroke-width="2.2"/></svg>
      </li>
      <li class="contacts__address"><span>End. completo, 00, Bairro<br>CEP 0000.000 - Cidade-SP</span>
        <svg viewBox="0 0 24 24" style="margin-top:3px"><path d="M12 2a7 7 0 0 0-7 7c0 5.3 7 13 7 13s7-7.7 7-13a7 7 0 0 0-7-7zm0 9.5A2.5 2.5 0 1 1 12 6.5a2.5 2.5 0 0 1 0 5z"/></svg>
      </li>
    </ul>

    <div class="website">www.prumoengenharia.com.br</div>
  </div>
</body>
</html>
```